Toravel Project Consulting

I need a logo and business card design for a small business operating in the management consulting and contractor space, predominantly in local and state government. I specialise in project management, financial consulting, people and culture, procurement, ICT transformation and contracting for corporate support areas of organisations.

Industry/Entity Type

Business

```html
<!DOCTYPE html>
<html lang="en">
<head>
<meta charset="utf-8">
<title>Toravel Project Consulting – Business Card</title>
<link rel="stylesheet" href="https://fonts.googleapis.com/css2?family=Raleway:wght@300;400;700;800&display=swap">
<style>
  :root {
    --backdrop: #c6e7de;
    --card: #ffffff;
    --brand-red: #ee1c25;
    --brand-grey: #8c8c8e;
    --text-light: #ffffff;
  }
  * { margin: 0; padding: 0; box-sizing: border-box; }
  html, body { width: 1200px; height: 856px; overflow: hidden; }
  body {
    background: var(--backdrop);
    font-family: "Raleway", sans-serif;
    display: flex;
    align-items: center;
    justify-content: center;
    gap: 60px;
  }
  .card {
    position: relative;
    width: 520px;
    height: 300px;
    border-radius: 26px;
    background: var(--card);
    overflow: hidden;
    box-shadow: 0 6px 18px rgba(40, 90, 80, 0.18);
  }

  /* Front */
  .card-front { display: flex; align-items: center; justify-content: center; }
  .wordmark { display: flex; align-items: center; gap: 14px; }
  .wordmark-square { width: 22px; height: 22px; background: var(--brand-red); flex: none; }
  .wordmark-name {
    color: var(--brand-grey);
    font-weight: 800;
    text-transform: uppercase;
    line-height: 1.05;
    letter-spacing: 0.04em;
  }
  .card-front .wordmark-name { font-size: 34px; }
  .card-front .wordmark-square { width: 26px; height: 26px; }

  /* Back */
  .back-shape { position: absolute; inset: 0; width: 100%; height: 100%; }
  .card-back .wordmark { position: absolute; left: 34px; top: 50%; transform: translateY(-50%); gap: 10px; }
  .card-back .wordmark-name { font-size: 19px; }
  .card-back .wordmark-square { width: 16px; height: 16px; }
  .holder {
    position: absolute;
    right: 34px;
    top: 30px;
    text-align: right;
    color: var(--text-light);
  }
  .holder-name { font-weight: 700; font-size: 20px; letter-spacing: 0.05em; text-transform: uppercase; }
  .holder-role { font-weight: 300; font-size: 14px; margin-top: 2px; }
  .address {
    position: absolute;
    right: 34px;
    bottom: 40px;
    text-align: right;
    color: var(--text-light);
    font-weight: 400;
    font-size: 14px;
    line-height: 1.4;
    font-style: normal;
  }
</style>
</head>
<body>
  <section class="card card-front" aria-label="Card front">
    <div class="wordmark">
      <span class="wordmark-square"></span>
      <span class="wordmark-name">Toravel<br>Project<br>Consulting</span>
    </div>
  </section>

  <section class="card card-back" aria-label="Card back">
    <svg class="back-shape" viewBox="0 0 520 300" preserveAspectRatio="none" aria-hidden="true">
      <path d="M218,0 C285,60 305,190 292,300 L520,300 L520,0 Z" fill="var(--brand-red)"/>
      <path d="M238,-4 C300,60 318,170 312,250" fill="none" stroke="var(--card)" stroke-width="6" stroke-linecap="round"/>
    </svg>
    <div class="wordmark">
      <span class="wordmark-square"></span>
      <span class="wordmark-name">Toravel<br>Project<br>Consulting</span>
    </div>
    <div class="holder">
      <p class="holder-name">Daniel Harlow</p>
      <p class="holder-role">Director</p>
    </div>
    <address class="address">14 Wexford Lane<br>Northbridge NSW 2063</address>
  </section>
</body>
</html>
```